Property Investment eBook Cover

I am a long established Australian property investment adviser, analyst and consultant who is now in semi-retired mode and have re-branded to reflect a more casual and personal approach to advising my property investor clients. I am writing a 'revised edition' to a book written in partnership with my father 20 years ago and need an eBook Cover for this new edition. The eBook will be uploaded to all the regular Australian providers (Larkfield Reader, Quince Folio, Tavi, Pagemarten)

The 3 key elements in the book cover are:

Title: The Harvest Engine of Land. The word 'Property' should be larger and more prominent. eg "The Wealth Power of" could be 1/3 the size of "Property" - with both justified left

Edition: Sydney 2021. "Sydney 2021" should be the focus and dominant imagery of the eBook cover and more prominent than the Title or Author

Author: Colin Marsh, The Housing Ledger Guide. The word "Author" should not appear. "The Housing Ledger Guide" should appear underneath Colin Marsh and justified to Colin Marsh, therefore a smaller font.

The cover should be simple, but eye-catching. No property images, more of an abstract background, than a background with an image. Our preferred colour palette is more blues/greens. Prefer SerifFonts

Copy of book published 20 years ago attached for reference only

```html
<!DOCTYPE html>
<html lang="en">
<head>
<meta charset="utf-8">
<title>The Harvest Engine of Land — Sydney 2021</title>
<link rel="stylesheet" href="https://fonts.googleapis.com/css2?family=Zilla+Slab:wght@700&family=Roboto+Condensed:wght@700&display=swap">
<style>
  :root {
    --backdrop: #9fb3b9;
    --cover-paper: #ebebe8;
    --panel-slate: #7f94a2;
    --panel-slate-light: #8ea2ae;
    --panel-slate-dark: #6f8593;
    --tag-orange: #e0694b;
    --cream: #f4ecd6;
  }
  * { margin: 0; padding: 0; box-sizing: border-box; }
  html, body {
    width: 1200px;
    height: 800px;
    overflow: hidden;
    background: var(--backdrop);
  }
  .canvas {
    position: relative;
    width: 1200px;
    height: 800px;
  }
  .cover {
    position: absolute;
    left: 340px;
    top: 30px;
    width: 520px;
    height: 740px;
    background: var(--cover-paper);
  }
  .cover-panel {
    position: absolute;
    left: 26px;
    top: 82px;
    width: 468px;
    height: 616px;
    background: radial-gradient(ellipse at 30% 25%, var(--panel-slate-light) 0%, var(--panel-slate) 55%, var(--panel-slate-dark) 100%);
  }
  .edition-tag {
    position: absolute;
    left: 6px;
    top: 52px;
    width: 190px;
    height: 44px;
    background: var(--tag-orange);
    clip-path: polygon(0 0, 100% 0, 88% 50%, 100% 100%, 0 100%);
    color: var(--cream);
    font-family: "Roboto Condensed", sans-serif;
    font-weight: 700;
    font-size: 29px;
    line-height: 44px;
    padding-left: 14px;
    letter-spacing: 0.2px;
  }
  .title {
    position: absolute;
    left: 30px;
    top: 58px;
    color: var(--cream);
    font-family: "Zilla Slab", serif;
    font-weight: 700;
  }
  .title-lead {
    display: block;
    font-size: 58px;
    line-height: 52px;
  }
  .title-key {
    display: block;
    font-size: 156px;
    line-height: 140px;
    margin-left: -4px;
  }
  .author {
    position: absolute;
    left: 34px;
    top: 452px;
    color: var(--cream);
    font-family: "Roboto Condensed", sans-serif;
    font-weight: 700;
  }
  .author-name {
    display: block;
    font-size: 20px;
    line-height: 24px;
  }
  .author-role {
    display: block;
    font-size: 11px;
    line-height: 16px;
  }
</style>
</head>
<body>
<main class="canvas">
  <article class="cover">
    <section class="cover-panel">
      <h1 class="title">
        <span class="title-lead">The</span>
        <span class="title-lead">Harvest</span>
        <span class="title-lead">Engine</span>
        <span class="title-lead">of</span>
        <span class="title-key">Land</span>
      </h1>
      <p class="author">
        <span class="author-name">Colin Marsh</span>
        <span class="author-role">The Housing Ledger Guide</span>
      </p>
    </section>
    <div class="edition-tag">Sydney 2021</div>
  </article>
</main>
</body>
</html>
```